Graphics for website image slider

We need 4 banners for website:

We provide software development services to very small to large Businesses. The focus of these 4 banners is to portray the four steps approach to our consulting process: Assess, Analyse, Plan and Deploy

Currently we have the following on our website:
http://www.lumertix.com

We are redesigning the website and want to use 4 sliding graphics to portray the same thing, and the new site is being designed here:
http://www.lumertixonline.com/lumertix

You can use stock photos for each banner or your own creativity.

The images should be 1140px wide and about 420px High.

You can use any modern font such as google font. Not just curly fonts!

Reason: Not yet able to select the final design.

I have updated the colors and how they are supposed to flow because I noticed that some designs did not follow that (We are consultants and really want to understand our process in a powerful way):

ASSESS: Orange color (1st or 5th color above)

ANALYSE: Yellow (2nd or 6th color above)

PLAN: Green (3rd or 7th color above)

DEPLOY: Blue (4th or 8th color above)

=================================================

Some designers also made mistakes in typing the text (Please copy and paste from below):

ASSESS

We gather information and data

to identify and delineate

your central and most pressing business and IT issues.

ANALYSE

We show you exactly where you are in terms of IT maturity

using our optimization tools.

We then build an IT roadmap to help you get to the next level.

PLAN:

We identify the IT products and processes necessary to implement the solution.

We then create a detailed plan of action and technical specifications.

DEPLOY

Finally, we utilize industry best practices and repeatable development and

deployment methods to ensure efficiency and high quality results

that satisfy and bring improvement within budget and timeline.

                                   

Target Market(s)

http://www.lumertix.com

Industry/Entity Type

Software

Font styles to use
Sans Serif
Other font styles liked:
• Any other modern font (No curly fonts)

Colors
fee18a
fbf289
cadf82
86cae6
f78f20
ffc214
9aca3c
0692cd

Requirements
Must have
• Graphic should convey the message for each process

```html
<!DOCTYPE html>
<html lang="en">
<head>
<meta charset="utf-8">
<title>Lumertix – Plan</title>
<link rel="stylesheet" href="https://fonts.googleapis.com/css2?family=Open+Sans:wght@300;400;600;700&display=swap">
<style>
  :root {
    --page-bg: #e9e9e9;
    --sheet-bg: #ffffff;
    --topbar-bg: #f3f3f3;
    --brand-red: #8b1a2b;
    --nav-text: #555555;
    --muted: #9a9a9a;
    --border: #d6d6d6;
    --step-green: #9aca3c;
    --step-green-light: #cadf82;
    --step-number: #6a6a6a;
    --body-text: #3a3a3a;
    --dot: #555555;
  }
  * { box-sizing: border-box; margin: 0; padding: 0; }
  html, body { width: 1200px; height: 665px; overflow: hidden; }
  body {
    position: relative;
    background: var(--page-bg);
    font-family: "Open Sans", Arial, sans-serif;
  }
  .site {
    position: absolute; left: 92px; top: 7px; width: 1020px; height: 658px;
    background: var(--sheet-bg);
    border-top: 4px solid var(--brand-red);
    border-radius: 3px 3px 0 0;
    box-shadow: 0 0 4px rgba(0,0,0,.12);
  }
  .topbar {
    position: absolute; left: 0; top: 0; width: 100%; height: 71px;
    background: var(--topbar-bg);
  }
  .round-btn {
    position: absolute; top: 26px; width: 25px; height: 25px; border-radius: 50%;
    background: #fff; box-shadow: 0 1px 3px rgba(0,0,0,.25);
    display: flex; align-items: center; justify-content: center;
  }
  .round-btn span { width: 9px; height: 9px; border-radius: 2px; background: #555; }
  .account-link {
    position: absolute; top: 33px; font-size: 10px; color: var(--brand-red);
    text-transform: uppercase; letter-spacing: .2px;
  }
  .search {
    position: absolute; left: 853px; top: 25px; width: 143px; height: 28px;
    border: 1px solid var(--border); border-radius: 14px; background: #fff;
    font-size: 11px; color: var(--muted); padding: 6px 11px;
  }
  .search svg { position: absolute; right: 10px; top: 8px; }
  .brand {
    position: absolute; left: 28px; top: 94px;
    font-size: 34px; font-weight: 700; color: var(--brand-red); letter-spacing: 1px;
  }
  .main-nav {
    position: absolute; top: 135px; font-size: 11px; font-weight: 700;
    color: var(--nav-text); text-transform: uppercase; white-space: nowrap;
  }
  .main-nav.is-active { color: var(--brand-red); }
  .slider {
    position: absolute; left: 25px; top: 189px; width: 970px; height: 416px;
    border-radius: 8px; overflow: hidden;
    background:
      radial-gradient(ellipse 40% 45% at 85% 45%, rgba(160,180,220,.85), rgba(160,180,220,0) 70%),
      radial-gradient(ellipse 35% 40% at 62% 40%, rgba(214,170,140,.8), rgba(214,170,140,0) 70%),
      linear-gradient(170deg, #4e4e4e 0%, #8a8a8a 22%, #d9d6d0 40%, #f2f1ee 62%, #e6c9a0 100%);
  }
  .step-number {
    position: absolute; left: 40px; top: 188px;
    font-size: 142px; font-weight: 300; line-height: 1; color: var(--step-number);
  }
  .step-label {
    position: absolute; left: 0; top: 286px; width: 217px; height: 71px;
    background: var(--step-green); color: #fff;
    font-size: 60px; line-height: 71px; padding-left: 48px;
  }
  .step-text {
    position: absolute; left: 217px; top: 286px; width: 470px; height: 71px;
    background: rgba(255,255,255,.82);
    border-bottom: 4px solid var(--step-green-light);
    padding: 10px 18px;
    font-size: 13px; line-height: 18px; color: var(--body-text);
  }
  .pager { position: absolute; right: 24px; bottom: 14px; display: flex; gap: 4px; }
  .pager span { width: 12px; height: 12px; border-radius: 50%; background: var(--dot); }
  .pager span.is-current { background: #fff; border: 3px solid var(--dot); }
</style>
</head>
<body>
  <div class="site">
    <div class="topbar">
      <div class="round-btn" style="left:25px"><span></span></div>
      <div class="round-btn" style="left:55px"><span></span></div>
      <div class="round-btn" style="left:85px"><span></span></div>

      <div class="round-btn" style="left:651px">
        <svg width="13" height="10" viewBox="0 0 13 10"><rect width="4.3" height="10" fill="#d8d8d8"/><rect x="4.3" width="4.4" height="10" fill="#f4f4f4"/><rect x="8.7" width="4.3" height="10" fill="#d8d8d8"/></svg>
      </div>
      <div class="round-btn" style="left:683px">
        <svg width="14" height="10" viewBox="0 0 14 10"><rect width="14" height="10" fill="#c8323c"/><rect y="2" width="14" height="1.4" fill="#fff"/><rect y="4.8" width="14" height="1.4" fill="#fff"/><rect y="7.6" width="14" height="1.4" fill="#fff"/><rect width="6" height="5" fill="#3a4a8c"/></svg>
      </div>

      <span class="account-link" style="left:732px">Register</span>
      <span class="account-link" style="left:799px">Login</span>

      <div class="search">Search...
        <svg width="11" height="11" viewBox="0 0 11 11"><circle cx="4.5" cy="4.5" r="3.5" fill="none" stroke="#bbb" stroke-width="1.5"/><line x1="7" y1="7" x2="10" y2="10" stroke="#bbb" stroke-width="1.5"/></svg>
      </div>
    </div>

    <div class="brand">LUMERTIX</div>

    <nav>
      <span class="main-nav is-active" style="left:431px">Home</span>
      <span class="main-nav" style="left:487px">About Us</span>
      <span class="main-nav" style="left:564px">Shop ⌄</span>
      <span class="main-nav" style="left:627px">Services ⌄</span>
      <span class="main-nav" style="left:708px">Portfolio</span>
      <span class="main-nav" style="left:791px">Blog</span>
      <span class="main-nav" style="left:845px">Careers</span>
      <span class="main-nav" style="left:915px">Contact Us</span>
    </nav>

    <section class="slider" role="img" aria-label="Photo of a hand writing with a pen on a printed project schedule chart next to a laptop">
      <div class="step-number">03</div>
      <div class="step-label">Plan</div>
      <p class="step-text">We identify the IT products and processes necessary to implement the solution. We then create a detailed plan of action and technical specifications.</p>
      <div class="pager"><span></span><span></span><span class="is-current"></span><span></span></div>
    </section>
  </div>
</body>
</html>
```